Need a banner made for my LinkedIn Profile

We are a sell side advisor and we need to update our LinkedIn banner
Amber Ridge offers two services:
1. Sell Side Advisory
2. And through our TetherMark program, Exit Readiness

Target Market(s)

Business owners, Private Equity Firms

Industry/Entity Type

Mergers and Acquisitions

Logo Text

Sell-Side Advisory Exit-Readiness

Font styles to use
Other font styles liked:
• Match logo fonts

Colors

Designer to choose colors to be used in the design.

Requirements
Must have
• Use the colors on the Amber Ridge Logo-All white background, use both logos

```html
<!DOCTYPE html>
<html lang="en">
<head>
<meta charset="UTF-8">
<title>Amber Ridge Capital – LinkedIn Banner</title>
<link href="https://fonts.googleapis.com/css2?family=Poppins:wght@600&display=swap" rel="stylesheet">
<style>
  :root {
    --ink: #0e1215;
    --teal: #2a8ca3;
    --white: #ffffff;
  }
  html, body {
    margin: 0;
    padding: 0;
    width: 1200px;
    height: 203px;
    overflow: hidden;
    background: var(--ink);
  }
  .banner {
    position: relative;
    width: 1200px;
    height: 203px;
    background: var(--ink);
    overflow: hidden;
    font-family: "Poppins", sans-serif;
    color: var(--white);
  }
  .services {
    position: absolute;
    left: 198px;
    top: 67px;
    margin: 0;
    padding: 0;
    list-style: none;
    font-size: 16.5px;
    font-weight: 600;
    line-height: 23px;
    letter-spacing: 0.2px;
  }
  .brand-name {
    position: absolute;
    left: 742px;
    top: 89px;
    margin: 0;
    font-size: 26px;
    font-weight: 600;
    line-height: 34px;
    letter-spacing: -0.4px;
    white-space: nowrap;
  }
  .wave {
    position: absolute;
    left: 0;
    bottom: 0;
    width: 1200px;
    height: 203px;
  }
  .wave path { fill: var(--teal); }
</style>
</head>
<body>
  <div class="banner">
    <ul class="services">
      <li>Sell-Side Advisory</li>
      <li>Exit-Readiness</li>
    </ul>

    <p class="brand-name">Amber Ridge Capital</p>

    <svg class="wave" viewBox="0 0 1200 203" preserveAspectRatio="none" aria-hidden="true">
      <path d="M0 160 C 60 154, 110 149, 170 150 C 330 152, 470 176, 620 175 C 720 174, 800 169, 880 169 C 1000 169, 1100 163, 1200 162 L 1200 203 L 0 203 Z"/>
    </svg>
  </div>
</body>
</html>
```